Surviving Domestic Violence Flyer

I need a flyer that "POPS" to attract participants for my research project. I have added the important information on my draft flyer.

```html
<!DOCTYPE html>
<html lang="en">
<head>
<meta charset="utf-8">
<title>Perceived Effectiveness of Domestic Violence Services – Study Flyer</title>
<link rel="stylesheet" href="https://fonts.googleapis.com/css2?family=Arimo:wght@400;700&family=Delius&family=Roboto+Condensed:wght@700;900&display=swap">
<style>
  :root {
    --navy: #2b3390;
    --deep-blue: #1f3a9e;
    --sky: #1ab0e8;
    --band: #c4e7f4;
    --cream: #fffdf0;
    --ink: #2c2c2c;
    --red: #e0232a;
    --yes: #b5203f;
    --edge: #8fc6e6;
  }
  * { box-sizing: border-box; margin: 0; padding: 0; }
  html, body { width: 847px; height: 1200px; overflow: hidden; background: #fff; }
  .flyer {
    position: relative; width: 847px; height: 1200px; overflow: hidden;
    background: linear-gradient(90deg, var(--edge), #d7ecf7 50%, var(--edge));
    font-family: "Arimo", Arial, sans-serif;
  }
  .page {
    position: absolute; left: 24px; right: 24px; top: 95px; bottom: 9px;
    background: var(--cream);
  }
  .edge-lines { position: absolute; top: 160px; width: 24px; height: 80px;
    background: repeating-linear-gradient(180deg, #fff 0 3px, transparent 3px 12px); }
  .edge-lines.left { left: 0; } .edge-lines.right { right: 0; }
  .edge-lines.low { top: 1080px; }
  .header {
    position: absolute; left: 0; top: 0; width: 100%; height: 95px;
    background: linear-gradient(90deg, #24309a, #1aa4e2 50%, #24309a);
    display: flex; align-items: center; justify-content: center;
  }
  .header h1 { font-family: "Delius", cursive; font-weight: 400; color: #fff; font-size: 35px; letter-spacing: 0.5px; }
  .footer-strip { position: absolute; left: 0; bottom: 0; width: 100%; height: 9px; background: linear-gradient(90deg, #24309a, #1aa4e2, #24309a); }
  .request { position: absolute; top: 103px; width: 100%; text-align: center;
    color: var(--sky); font-weight: 700; font-size: 46px; letter-spacing: 0.3px; }
  .subtitle { position: absolute; top: 180px; width: 100%; text-align: center;
    color: var(--navy); font-weight: 700; font-size: 22.5px; line-height: 31px; }
  .criteria { position: absolute; left: 50px; top: 263px; list-style: none; color: var(--ink); font-size: 21.5px; line-height: 35.5px; }
  .criteria li { position: relative; padding-left: 30px; }
  .criteria li::before { content: ""; position: absolute; left: 0; top: 12px; width: 14px; height: 14px; border-radius: 50%; background: var(--red); }
  .eligibility {
    position: absolute; left: 24px; right: 24px; top: 481px; height: 289px;
    background: var(--band); text-align: center; color: var(--navy);
    font-family: "Roboto Condensed", "Arial Narrow", sans-serif; font-weight: 700;
  }
  .eligibility .lead { margin-top: 17px; font-size: 24px; }
  .eligibility .yes { font-weight: 900; color: var(--yes); font-size: 62px; line-height: 62px; margin-top: 8px; }
  .eligibility .body { font-size: 24.5px; line-height: 36.5px; margin-top: 2px; }
  .target-art { position: absolute; left: 0; top: 780px; width: 440px; height: 420px; }
  .contact { position: absolute; left: 325px; width: 500px; top: 790px; text-align: center; color: #222; }
  .contact .line { font-size: 19px; line-height: 22px; }
  .contact .phone { color: var(--navy); font-weight: 700; font-size: 33px; line-height: 40px; }
  .contact .comp { color: var(--sky); font-weight: 700; font-size: 29.5px; line-height: 35px; margin-top: 6px; }
  .contact .label { font-size: 15px; line-height: 17px; color: #555; }
  .contact .value { font-size: 23px; line-height: 26px; color: #444; }
</style>
</head>
<body>
<div class="flyer">
  <div class="edge-lines left"></div><div class="edge-lines right"></div>
  <div class="edge-lines left low"></div><div class="edge-lines right low"></div>
  <div class="page"></div>
  <header class="header"><h1>"Perceived Effectiveness of Domestic Violence Services"</h1></header>

  <h2 class="request">Request for Study Participants</h2>
  <p class="subtitle">EFFICIENCY OF RESOURCES AVAILABLE TO SUVIVORS<br>OF INTIMATE PARTNER ABUSE</p>

  <ul class="criteria">
    <li>Are you eighteen years of age or older?</li>
    <li>Have you been a victim of domestic violence?</li>
    <li>Have you sought assistance with abuse in the last 12 months?</li>
    <li>Are you still in contact with the person who abused you?</li>
    <li>Are you willing and open to discussing your experience with<br>abuse and your attempts to access services or resources?</li>
  </ul>

  <section class="eligibility">
    <p class="lead">If you answered</p>
    <p class="yes">Yes</p>
    <p class="body">to all of these questions,<br>you may be eligible to participate in a study to better<br>understand the resources needed and services expected<br>for survivours of domestic violence.</p>
  </section>

  <svg class="target-art" role="img" aria-label="Illustration of a blue and white target with an orange arrow striking the bullseye" viewBox="0 0 440 420">
    <defs>
      <radialGradient id="targetTone" cx="0.27" cy="0.55" r="0.75">
        <stop offset="0" stop-color="#2a63c8"/>
        <stop offset="0.45" stop-color="#7fb0e6"/>
        <stop offset="1" stop-color="#fffdf0" stop-opacity="0"/>
      </radialGradient>
    </defs>
    <rect width="440" height="420" fill="url(#targetTone)"/>
  </svg>

  <section class="contact">
    <p class="line">Please contact Dana Whitfield at</p>
    <p class="phone">1(555)014-2286</p>
    <p class="line">or via e-mail:</p>
    <p class="line">safepathstudy@examplemail.com for<br>additional information</p>
    <p class="comp">Participants will be<br>compensated for their time</p>
    <p class="label">Principal Investigator:</p>
    <p class="value">Dana Whitfield</p>
    <p class="label">Institutional Affiliation:</p>
    <p class="value">Lakeshore State University,<br>Dept. of Criminology, Law, and Justice</p>
    <p class="label">Contact Address:</p>
    <p class="value">Post Office Box 381204, Easton, IL, 60611</p>
  </section>

  <div class="footer-strip"></div>
</div>
</body>
</html>
```